Business Card Design

I already have a company logo for my company. I have a logo for the manufacturer we represent. I want a professional business card design.

```html
<!DOCTYPE html>
<html lang="en">
<head>
<meta charset="utf-8">
<title>Alertline Systems – Business Card</title>
<link href="https://fonts.googleapis.com/css2?family=Open+Sans:wght@400;600;700;800&display=swap" rel="stylesheet">
<style>
  :root {
    --backdrop: #222222;
    --card: #ffffff;
    --ink: #1c1c1c;
    --brand-red: #e3242b;
    --brand-gold: #c9971f;
    --rule: #2a2a2a;
  }
  * { box-sizing: border-box; margin: 0; padding: 0; }
  html, body {
    width: 1200px; height: 780px; overflow: hidden;
    background: var(--backdrop);
    font-family: "Open Sans", Arial, sans-serif;
    color: var(--ink);
  }
  .sheet {
    width: 1200px; height: 780px;
    display: flex; align-items: center; justify-content: center; gap: 40px;
  }
  .card {
    position: relative;
    width: 520px; height: 297px;
    background: var(--card);
    box-shadow: 0 14px 30px rgba(0,0,0,.45);
  }

  /* brand wordmark */
  .brand { display: flex; align-items: center; gap: 10px; }
  .brand__mark { width: 22px; height: 22px; background: var(--brand-red); flex: none; }
  .brand__name {
    font-weight: 800; color: var(--brand-red);
    text-transform: uppercase; line-height: 1.05; letter-spacing: .5px;
  }

  /* front */
  .front .brand { position: absolute; left: 44px; top: 78px; }
  .front .brand__name { font-size: 21px; }
  .front .divider {
    position: absolute; left: 262px; top: 58px;
    width: 1px; height: 156px; background: var(--rule);
  }
  .front .address {
    position: absolute; left: 40px; bottom: 34px;
    font-size: 13px; letter-spacing: .2px;
  }
  .holder { position: absolute; left: 290px; top: 72px; }
  .holder__name { font-size: 27px; font-weight: 700; line-height: 1.1; }
  .holder__first { color: var(--brand-red); }
  .holder__last { color: var(--brand-gold); }
  .holder__role { font-size: 14px; font-weight: 600; margin-top: 2px; }
  .contacts { list-style: none; margin-top: 16px; font-size: 13px; line-height: 1.55; }
  .contacts li { display: flex; align-items: center; gap: 8px; }
  .contacts svg { width: 11px; height: 11px; flex: none; }

  /* back */
  .back { display: flex; align-items: center; justify-content: center; }
  .back .brand { gap: 14px; }
  .back .brand__mark { width: 34px; height: 34px; }
  .back .brand__name { font-size: 32px; }
</style>
</head>
<body>
<main class="sheet">

  <section class="card front" aria-label="Business card front">
    <div class="brand">
      <span class="brand__mark"></span>
      <span class="brand__name">Alertline<br>Systems LLC</span>
    </div>

    <span class="divider"></span>

    <div class="holder">
      <h1 class="holder__name"><span class="holder__first">Daniel</span> <span class="holder__last">Horvath</span></h1>
      <p class="holder__role">Managing Director</p>
      <ul class="contacts">
        <li>
          <svg viewBox="0 0 12 12" aria-hidden="true"><path fill="var(--brand-red)" d="M2.4 0.8l2 2-1 1.3c.7 1.5 1.8 2.6 3.4 3.4l1.3-1 2 2-1.2 1.7C4.9 10 1.9 7 1 2z"/></svg>
          (555) 214-0386
        </li>
        <li>
          <svg viewBox="0 0 12 12" aria-hidden="true"><rect x="0.5" y="2" width="11" height="8" rx="1" fill="var(--brand-red)"/><path d="M1 2.6L6 6.6l5-4" fill="none" stroke="#fff" stroke-width="1"/></svg>
          info@alertlinesys.com
        </li>
        <li>
          <svg viewBox="0 0 12 12" aria-hidden="true"><circle cx="6" cy="6" r="5.5" fill="var(--brand-red)"/><path d="M0.8 6h10.4M6 .6c-2.6 3-2.6 7.8 0 10.8M6 .6c2.6 3 2.6 7.8 0 10.8" fill="none" stroke="#fff" stroke-width=".8"/></svg>
          www.alertlinesys.com
        </li>
      </ul>
    </div>

    <p class="address">1480 Meadowbrook Ave. Suite 300 Dalton, TX 75010</p>
  </section>

  <section class="card back" aria-label="Business card back">
    <div class="brand">
      <span class="brand__mark"></span>
      <span class="brand__name">Alertline<br>Systems LLC</span>
    </div>
  </section>

</main>
</body>
</html>
```